Up to the Challenge? Canadian based consulting company needs a two sided business card design

A Canadian based security risk management consulting company needs a two-sided business card design. What we do is provide advice and guidance related to emergency, security and business continuity management for small, medium and large companies to help ensure the protection of their people, assets, information, services, operations and reputation.

The final design should be simple, only one or two colours, eye catching, professional and one that makes people look at three or more times just because it looks so darn good.

I have include examples of business cards I like.

Target Market(s)

Small, medium and large companies.

Industry/Entity Type

Security

Contact Information for Business Card

Business Card Size: Standard size of 3.5" (89mm) x 2.0" (51mm) - (see full specifications and guides on PRINTA's website if required)
Card Stock: Looking to use PRINTA's Velda 32pt stock textured paper - seam colour either chili red or black
Business Name: The Harrowfield Group
Website: www.theharrowfieldgroup.example
Telephone: (555)214-0397
Name: Dana Forsythe
Position: Principle
e-mail: Dana.Forsythe@theharrowfieldgroup.example

Font styles to use
Serif

Colors
ec1f27
000000
9d9d9d
aaaaaa
606060

Requirements
Must have
• - "The Harrowfield Group" logo (see uploaded files). I have included grey scale and colour versions.
• - Business card details (as above)
Nice to have
• - One side black or grey scale.
• - Other side would likely be white.
• - Everyone likes the silver logo on the black background.
• - Small element of colour i.e. red but I'm leaning more to greyscale.
Should not have
• - A lot of colour. Keep it simple.

```html
<!DOCTYPE html>
<html lang="en">
<head>
<meta charset="utf-8">
<title>The Harrowfield Group — Business Card</title>
<link rel="stylesheet" href="https://fonts.googleapis.com/css2?family=Tinos:wght@400;700&display=swap">
<style>
  :root {
    --brand-red: #ec1f27;
    --ink-black: #000000;
    --stone-grey: #9d9d9d;
    --silver-grey: #aaaaaa;
    --slate-grey: #606060;
    --paper-white: #f4f4f2;
    --backdrop: #e3e2df;
    --card-ink: #1a1a1a;
  }
  * { box-sizing: border-box; margin: 0; padding: 0; }
  html, body {
    width: 1200px;
    height: 800px;
    overflow: hidden;
  }
  body {
    background: var(--backdrop);
    font-family: "Tinos", "Times New Roman", serif;
    display: flex;
    align-items: center;
    justify-content: center;
    gap: 50px;
  }
  .card {
    position: relative;
    width: 525px;
    height: 300px;
    box-shadow: 0 10px 24px rgba(0, 0, 0, 0.18);
  }

  /* Front: white personal side */
  .card-front {
    background: var(--paper-white);
    color: var(--card-ink);
  }
  .holder-name {
    position: absolute;
    top: 56px;
    left: 0;
    right: 0;
    text-align: center;
    font-size: 46px;
    font-weight: 700;
    letter-spacing: 0.5px;
  }
  .holder-role {
    position: absolute;
    top: 112px;
    left: 0;
    right: 0;
    text-align: center;
    padding-left: 40px;
    font-size: 18px;
    font-weight: 700;
    color: var(--brand-red);
  }
  .front-rule {
    position: absolute;
    top: 146px;
    left: 60px;
    right: 60px;
    height: 1px;
    background: var(--slate-grey);
  }
  .contact-list {
    position: absolute;
    top: 162px;
    left: 60px;
    list-style: none;
    font-size: 13px;
    line-height: 1.6;
    color: var(--brand-red);
  }

  /* Back: black brand side */
  .card-back {
    background: #0c0c0c;
  }
  .brand-lockup {
    position: absolute;
    top: 78px;
    left: 0;
    right: 0;
    display: flex;
    flex-direction: column;
    align-items: center;
    gap: 14px;
  }
  .brand-mark {
    width: 46px;
    height: 46px;
    background: var(--slate-grey);
  }
  .brand-name {
    font-size: 17px;
    font-weight: 700;
    letter-spacing: 2px;
    text-transform: uppercase;
    color: var(--brand-red);
  }
  .back-rule {
    position: absolute;
    top: 178px;
    left: 90px;
    right: 90px;
    height: 1px;
    background: var(--brand-red);
  }
</style>
</head>
<body>
  <section class="card card-front" aria-label="Card front">
    <h1 class="holder-name">Dana Forsythe</h1>
    <p class="holder-role">Principle</p>
    <div class="front-rule"></div>
    <ul class="contact-list">
      <li>Tel : (555)214-0397</li>
      <li>E-Mail : Dana.Forsythe@theharrowfieldgroup.example</li>
      <li>Web : www.theharrowfieldgroup.example</li>
    </ul>
  </section>

  <section class="card card-back" aria-label="Card back">
    <div class="brand-lockup">
      <span class="brand-mark"></span>
      <span class="brand-name">The Harrowfield Group</span>
    </div>
    <div class="back-rule"></div>
  </section>
</body>
</html>
```